Flyer Design Project

Something bold, something creative, something colorful. Will have 3 full time employees passing these out to business owners locally as well as national conventions.
Need something that will grab attention and remain a reminder, before they end up hitting the trash can...
Site can be found at www.KelvoraPress.example
A few different logo formats are attached.
2 sizes would be nice. 8.5" x 11" and 4"x6 (they can look the same)
No specifics on graphics, colors or info. Stay somewhat consistent with the website. I basically just want people to know we are here and we are definitely the cheapest print prices in the nation.
Target Market(s)
Anyone that needs print work done.
Industry/Entity Type
Business
Look and feel
Each slider illustrates characteristics of the customer's brand and the style your logo design should communicate.

```html
<!DOCTYPE html>
<html lang="en">
<head>
<meta charset="utf-8">
<title>Kelvora Press Flyer</title>
<link href="https://fonts.googleapis.com/css2?family=Arimo:wght@400;700&display=swap" rel="stylesheet">
<style>
  :root {
    --backdrop: #262626;
    --olive: #4c5e31;
    --orange: #f26b2b;
    --lime: #8dc63f;
    --lime-text: #9ccb3b;
    --title-green: #3e5a1f;
    --ink: #1e1e1e;
    --logo-grey: #3a3a3a;
    --white: #ffffff;
  }
  * { margin: 0; padding: 0; box-sizing: border-box; }
  html, body {
    width: 1200px; height: 750px; overflow: hidden;
    background: var(--backdrop);
    font-family: "Arimo", Arial, sans-serif;
  }
  .stage { position: relative; width: 1200px; height: 750px; }
  .flyer {
    position: absolute; left: 372px; top: 81px;
    width: 455px; height: 588px;
    transform: scale(1.14); transform-origin: center center;
    background: var(--white); overflow: hidden;
  }
  .hero-photo {
    position: absolute; left: 0; top: 0; width: 455px; height: 208px;
    background:
      radial-gradient(ellipse at 55% 70%, #2d3f5c 0%, #3d5270 22%, rgba(61,82,112,0) 48%),
      linear-gradient(100deg, #dfe9f2 0%, #f6f9fc 35%, #cfdbe8 70%, #e8eef5 100%);
  }
  .headline-band {
    position: absolute; left: 0; top: 208px; width: 455px; height: 104px;
    background: var(--olive); color: var(--white); font-weight: 700;
  }
  .headline-band .line { position: absolute; white-space: nowrap; }
  .line-one { left: 14px; top: 12px; font-size: 19px; }
  .line-two { left: 87px; top: 44px; font-size: 19px; }
  .accent { color: var(--orange); font-size: 26px; }
  .guarantee { left: 250px; top: 76px; font-size: 15px; color: var(--lime-text); }
  .product-list {
    position: absolute; left: 0; top: 312px; width: 88px; height: 178px;
    background: var(--orange); list-style: none; padding: 10px 0 0 11px;
    color: var(--white); font-weight: 700; font-size: 8px; line-height: 10.2px;
  }
  .brand-panel {
    position: absolute; left: 88px; top: 312px; width: 367px; height: 91px;
    background: var(--white); display: flex; align-items: center; padding-left: 24px;
  }
  .brand-dot { width: 54px; height: 54px; border-radius: 50%; background: var(--orange); flex: none; }
  .brand-text { margin-left: 22px; color: var(--logo-grey); }
  .brand-name { font-size: 38px; font-weight: 400; line-height: 1; white-space: nowrap; }
  .brand-tagline { font-size: 13px; margin-top: 4px; margin-left: 22px; }
  .info-panel {
    position: absolute; left: 88px; top: 403px; width: 367px; height: 87px;
    background: var(--lime); padding: 6px 10px 0 14px;
  }
  .info-title { font-size: 13px; font-weight: 700; color: var(--title-green); margin-bottom: 3px; }
  .info-body { font-size: 6.2px; line-height: 8.4px; color: var(--ink); font-weight: 700; }
  .contact-band {
    position: absolute; left: 0; top: 490px; width: 455px; height: 98px;
    background: var(--olive); color: var(--white); font-weight: 700;
  }
  .pitch { position: absolute; left: 12px; top: 11px; font-size: 11px; line-height: 18px; white-space: nowrap; }
  .support { position: absolute; left: 20px; top: 60px; font-size: 19px; word-spacing: 2px; white-space: nowrap; }
  .support .phone { margin-left: 10px; }
</style>
</head>
<body>
<div class="stage">
  <article class="flyer">
    <div class="hero-photo" role="img" aria-label="Photo of three smiling office workers giving a thumbs up beside a laptop in a bright office"></div>

    <header class="headline-band">
      <div class="line line-one">NOBODY <span class="accent">BEATS</span></div>
      <div class="line line-two">OUR PRINTS <span class="accent">PRICES!</span></div>
      <div class="line guarantee">100% GUARANTEED</div>
    </header>

    <ul class="product-list">
      <li>Business Card</li><li>Booklet</li><li>Bookmark</li><li>Brochure</li>
      <li>Calendar</li><li>Catalog</li><li>CD Package</li><li>Club Flyer</li>
      <li>Collectors Card</li><li>Door Hanger</li><li>DVD Package</li><li>Envelope</li>
      <li>Event Ticket</li><li>Flyer</li><li>Hang Tag</li><li>Letterhead</li>
    </ul>

    <section class="brand-panel">
      <span class="brand-dot"></span>
      <div class="brand-text">
        <div class="brand-name">Kelvora Press</div>
        <div class="brand-tagline">Discount Print and Promo</div>
      </div>
    </section>

    <section class="info-panel">
      <h2 class="info-title">YOUR TITLE WILLCOME HERE</h2>
      <p class="info-body">Lorem Ipsum is simply dummy text of the printing and typesetting industry. Lorem Ipsum has been the industry's standard dummy text ever since the 1500s, when an unknown printer took a galley of type and scrambled it to make a type specimen book. It has survived not only five centuries, but also the leap into electronic typesetting, remaining essentially unchanged. It was popularised in the 1960s with the release of transfer sheets containing Lorem Ipsum passages, and more recently with desktop publishing and page layout software including versions of Lorem Ipsum.</p>
    </section>

    <footer class="contact-band">
      <p class="pitch">Need high quality business cards, flyers, postcards, brochures, or catalogs?<br>Look no further than KelvoraPress.example!</p>
      <p class="support">CUSTOMER SUPPORT <span class="phone">(888) 555. 0142</span></p>
    </footer>
  </article>
</div>
</body>
</html>
```